Business card for exciting VC company

Should look simple, crisp, and modern.

Industry/Entity Type

Venture Capital

Contact Information for Business Card

Would like to see at least one design that has our blue on the back with the tagline "Transforming Traditional Industry" and white front with contact details.

Font styles to use
Sans Serif

Requirements
Must have
• Logo

Gregory Tallis
gtallis@brindlewave.vc
Managing Partner
M (628)354-xxxx

```html
<!DOCTYPE html>
<html lang="en">
<head>
<meta charset="utf-8">
<title>Brindlewave Capital – Business Card</title>
<link href="https://fonts.googleapis.com/css2?family=Roboto:wght@400;500;700&display=swap" rel="stylesheet">
<style>
  :root {
    --stage: #2c2c2e;
    --card-back: #9ea2a8;
    --card-front: #ffffff;
    --brand-blue: #4181c6;
    --ink: #111111;
    --ink-soft: #333333;
  }
  * { box-sizing: border-box; margin: 0; padding: 0; }
  html, body {
    width: 1200px; height: 1200px; overflow: hidden;
    background: var(--stage);
    font-family: "Roboto", Arial, sans-serif;
  }
  .canvas {
    position: relative; width: 1200px; height: 1200px;
  }
  .card {
    position: absolute; left: 150px; width: 900px; height: 500px;
    border-radius: 40px; overflow: hidden;
    box-shadow: 0 18px 40px rgba(0,0,0,0.45);
  }
  .card--back { top: 70px; background: var(--card-back); }
  .card--front { top: 630px; background: var(--card-front); }

  .wordmark {
    position: absolute; left: 0; right: 0; text-align: center;
    font-weight: 500; color: var(--ink);
    font-size: 50px; letter-spacing: 0.14em;
  }
  .card--back .wordmark { top: 180px; }
  .card--front .wordmark { top: 120px; }

  .tagline {
    position: absolute; left: 0; right: 0; bottom: 70px; text-align: center;
    font-size: 17px; font-weight: 500; letter-spacing: 0.32em;
    color: var(--ink);
  }

  .contact {
    position: absolute; left: 120px; top: 320px;
    display: flex; align-items: stretch; gap: 26px;
  }
  .contact__person { text-align: right; }
  .contact__name {
    color: var(--brand-blue); font-weight: 700; font-size: 30px;
    text-transform: uppercase; letter-spacing: 0.01em;
  }
  .contact__role {
    color: var(--ink-soft); font-size: 21px; margin-top: 4px;
  }
  .contact__divider { width: 2px; background: var(--brand-blue); }
  .contact__lines { display: flex; flex-direction: column; justify-content: center; gap: 8px; }
  .contact__line {
    display: flex; align-items: center; gap: 10px;
    color: var(--ink-soft); font-size: 22px;
  }
  .contact__icon { width: 24px; height: 24px; flex: none; }

  .card__band {
    position: absolute; left: 0; right: 0; bottom: 0; height: 40px;
    background: var(--brand-blue);
  }
</style>
</head>
<body>
<main class="canvas">
  <section class="card card--back" aria-label="Card back">
    <div class="wordmark">BRINDLEWAVE CAPITAL</div>
    <p class="tagline">TRANSFORMING TRADITIONAL INDUSTRY</p>
  </section>

  <section class="card card--front" aria-label="Card front">
    <div class="wordmark">BRINDLEWAVE CAPITAL</div>
    <div class="contact">
      <div class="contact__person">
        <p class="contact__name">Gregory Tallis</p>
        <p class="contact__role">Managing Partner</p>
      </div>
      <div class="contact__divider"></div>
      <div class="contact__lines">
        <p class="contact__line">
          <svg class="contact__icon" viewBox="0 0 24 24" aria-hidden="true">
            <circle cx="12" cy="12" r="12" fill="#4181c6"/>
            <path d="M8.6 6.5l1.8 2.4c.3.4.2.9-.1 1.2l-.9.8c.7 1.5 1.9 2.8 3.5 3.6l.8-.9c.3-.3.8-.4 1.2-.1l2.4 1.8c.4.3.5.9.1 1.3l-1 1.1c-.6.6-1.5.8-2.3.5-3.4-1.3-6-3.9-7.2-7.3-.3-.8-.1-1.7.5-2.3l1-1c.4-.4 1-.3 1.3.1z" fill="#fff"/>
          </svg>
          (628)354-xxxx
        </p>
        <p class="contact__line">
          <svg class="contact__icon" viewBox="0 0 24 24" aria-hidden="true">
            <circle cx="12" cy="12" r="12" fill="#4181c6"/>
            <rect x="6" y="8" width="12" height="8.5" rx="1" fill="none" stroke="#fff" stroke-width="1.5"/>
            <path d="M6.5 8.7L12 13l5.5-4.3" fill="none" stroke="#fff" stroke-width="1.5"/>
          </svg>
          gtallis@brindlewave.vc
        </p>
      </div>
    </div>
    <div class="card__band"></div>
  </section>
</main>
</body>
</html>
```